Corvel Lending Systems Re-design.

Quorvane have recently launched a new site using Brickloft CMS system (http://www.corvellendingsystems.example.com.au). We are looking to update the look and feel to match the rest of our brands (http://www.velnarix.example.com.au and http://www.tidelark.example.com.au) We are keen for the design to be more visually engaging, incorporating more imagery and create a clean and easy to navigate interface.

We are looking for 2 pages to be designed. The first page would be the homepage which should contain the following:
Menu to the sub categories provided in the site map.
Room for latest news articles
Small area for polls
Contact us section
Page 2 should offer a content page. An example of this would be CRM (sales Platform) from the site map. This page would need to contain an overall description of the product and menu to the following:
Flash Demo.
Features and Benefits.
Enquire now.

Target Market(s)

Quorvane offer software and web tools that enable Mortgage brokers to manage their clients, choose the most applicable loan and submit applications to the lender (bank).
The target market for this site is mainly mortgage brokers and the banking industry (lenders, Brokerages and Aggregators of homeloans).
Mortgage brokers often work in small brokerages or are self employed running their business within the local community, alternatively they may own a franchise business such as Brindle Key Finance, ZOLT or Lender Harbour.

Industry/Entity Type

Software

Number of Pages Required

2 pages

Requirements
Must have
• Must suitably match the look and feel of our sister companies velnarix.example.com.au and tidelark.example.com.au and our group site corvelgroup.example.com.au.
Colour scheme should not differ from the base logo colours provided.
Should not have
• Although Quorvane offers mortgage software to brokers we do not sell homeloans or deal directly with buyers, therefore pictures of houses and a look you see from lenders is not what we are looking for. Our customers are Mortgage brokers and top tier banks.

```html
<!DOCTYPE html>
<html lang="en">
<head>
<meta charset="utf-8">
<title>Quorvane Lending Systems – Home</title>
<link rel="stylesheet" href="https://fonts.googleapis.com/css2?family=Alfa+Slab+One&family=Cabin:wght@400;500;600&family=Noto+Sans:wght@400;700&display=swap">
<style>
:root{
  --crimson:#a8002f;
  --crimson-dark:#7c0021;
  --crimson-deep:#5e0018;
  --page:#dce2e9;
  --header:#dfe5ec;
  --ink:#111111;
  --ink-soft:#222222;
  --lilac:#b9b5d6;
  --hero-night:#2a2640;
  --hero-violet:#3f3763;
  --sky-light:#e9eef2;
  --sky-mid:#b8c7d5;
  --white:#ffffff;
  --field:#e2e4e8;
  --button-top:#c9cbe4;
  --button-bottom:#9a9cc4;
}
*{box-sizing:border-box;margin:0;padding:0}
html,body{width:1018px;height:1200px;overflow:hidden}
body{background:var(--page);font-family:"Noto Sans",Tahoma,sans-serif;color:var(--ink);position:relative}
.site-header{position:absolute;left:0;top:0;width:1018px;height:110px;background:linear-gradient(90deg,#e8ecf1,var(--header) 40%,#d9dfe7)}
.brand{position:absolute;left:31px;top:24px;display:flex;align-items:center;gap:10px;font-family:"Cabin",sans-serif;font-weight:600;font-size:46px;line-height:1;color:var(--crimson);letter-spacing:-1px}
.brand-dot{width:13px;height:13px;border-radius:50%;background:var(--crimson)}
.poll{position:absolute;left:745px;top:24px;width:245px}
.poll-title{font-family:"Cabin",sans-serif;font-size:17px;color:var(--crimson);line-height:1}
.poll-form{display:flex;gap:3px;margin-top:4px}
.poll-fields{display:flex;flex-direction:column;gap:3px}
.poll-field{width:167px;height:18px;border:1px solid #a9adb3;background:var(--field);font-size:10px;color:#7d8088;padding:2px 5px;font-family:"Noto Sans",sans-serif}
.poll-submit{width:71px;height:39px;border:1px solid #7e80a8;background:linear-gradient(var(--button-top),var(--button-bottom));font-family:"Cabin",sans-serif;font-size:16px;color:var(--ink)}
.main-nav{position:absolute;left:0;top:110px;width:1018px;height:58px;border-top:3px solid #25121a;background:linear-gradient(var(--crimson) 0%,#9a002b 60%,var(--crimson-dark) 100%);display:flex;justify-content:center;align-items:center}
.main-nav a{font-family:"Cabin",sans-serif;font-size:15.5px;color:var(--white);text-decoration:none;padding:0 10px;letter-spacing:.2px}
.main-nav a.is-current{color:var(--lilac)}
.hero{position:absolute;left:0;top:170px;width:1018px;height:412px;background:repeating-linear-gradient(90deg,var(--hero-night) 0 14px,var(--hero-violet) 14px 20px,#312b4d 20px 31px)}
.hero-frame{position:absolute;left:30px;top:28px;width:957px;height:357px;background:var(--white);padding:10px}
.hero-panel{position:relative;width:100%;height:100%;background:linear-gradient(100deg,#e6ebf0 0%,#cdd8e2 45%,var(--sky-mid) 100%);overflow:hidden}
.hero-visual{position:absolute;right:0;top:0;width:560px;height:100%;background:radial-gradient(ellipse 60% 55% at 58% 42%,rgba(240,243,246,.9) 0%,rgba(200,212,224,.5) 55%,rgba(180,198,214,0) 100%)}
.hero-copy{position:absolute;left:16px;top:94px}
.hero-kicker{font-family:"Alfa Slab One",serif;font-size:27px;color:var(--crimson);letter-spacing:1px;line-height:1}
.hero-title{font-family:"Cabin",sans-serif;font-weight:500;font-size:34px;line-height:37px;color:var(--ink-soft);margin-top:6px}
.hero-button{display:inline-block;margin-top:12px;margin-left:3px;padding:5px 9px;border:1px solid #7e80a8;background:linear-gradient(var(--button-top),var(--button-bottom));font-weight:700;font-size:11px;color:var(--ink)}
.intro{position:absolute;left:31px;top:592px;width:708px}
.section-title{font-family:"Cabin",sans-serif;font-size:17px;color:var(--ink);line-height:1}
.section-title strong{font-weight:400;font-size:28px;color:var(--crimson)}
.intro .section-title{padding-bottom:6px;border-bottom:1px dotted var(--crimson)}
.intro-body{font-size:11px;line-height:14px;color:var(--ink-soft);margin-top:12px}
.intro-body p{margin-bottom:15px}
.intro-body b{font-weight:700;font-size:11.5px;color:var(--ink)}
.firsts{list-style:none;margin:2px 0 16px 54px}
.firsts li{font-weight:700;font-size:12px;line-height:14.5px;color:var(--ink)}
.firsts li::before{content:"•";margin-right:11px;margin-left:-16px}
.news{position:absolute;left:752px;top:592px;width:236px}
.news-list{margin-top:8px;border:1px solid var(--crimson-deep);background:var(--crimson)}
.news-item{padding:9px 10px 8px 20px;border-bottom:1px solid #c0385b;color:var(--white)}
.news-item h3{font-weight:700;font-size:11px;line-height:14px}
.news-item time{display:block;font-size:9px;margin-top:5px;letter-spacing:.2px}
.news-more{display:flex;justify-content:center;gap:22px;align-items:center;background:var(--crimson-dark);height:28px;font-weight:700;font-size:11px;color:#ffe55c}
.news-more .mark{color:var(--white);font-size:9px}
.contact{position:absolute;left:752px;top:912px;width:236px}
.contact-card{position:relative;margin-top:10px;height:171px;border:3px solid #4a4a4a;background:var(--white);overflow:hidden}
.contact-visual{position:absolute;left:0;top:0;width:130px;height:115px;background:radial-gradient(ellipse at 35% 40%,#cfd3d8 0%,#eceef0 60%,rgba(255,255,255,0) 100%)}
.contact-lines{position:absolute;right:10px;top:4px;text-align:right;font-weight:700}
.contact-lines dt{font-size:12.5px;color:var(--ink);margin-top:11px}
.contact-lines dt:first-child{margin-top:0}
.contact-lines dd{font-size:14px;color:var(--crimson);line-height:17px}
.site-footer{position:absolute;left:0;top:1131px;width:1018px;height:69px;border-top:3px solid #25121a;background:linear-gradient(var(--crimson),var(--crimson-dark));text-align:center;color:var(--white);font-size:10.5px;padding-top:17px}
.footer-nav a{color:var(--white);text-decoration:none}
.footer-nav .sep{margin:0 8px}
.legal{margin-top:1px}
</style>
</head>
<body>
<header class="site-header">
  <div class="brand"><span class="brand-dot"></span>Quorvane</div>
  <form class="poll">
    <div class="poll-title">Give Your Poll</div>
    <div class="poll-form">
      <div class="poll-fields">
        <input class="poll-field" type="text" placeholder="Your Name">
        <input class="poll-field" type="text" placeholder="Email Id">
      </div>
      <button class="poll-submit" type="button">Submit</button>
    </div>
  </form>
</header>

<nav class="main-nav">
  <a class="is-current" href="#">HOME</a>
  <a href="#">MORTGAGE SOLUTIONS</a>
  <a href="#">MESSAGING</a>
  <a href="#">COMPANY</a>
  <a href="#">NEWS</a>
  <a href="#">SUPPORT</a>
  <a href="#">PRIVACY POLICY</a>
  <a href="#">SITE MAP</a>
  <a href="#">CONTACT US</a>
</nav>

<section class="hero">
  <div class="hero-frame">
    <div class="hero-panel">
      <div class="hero-visual" role="img" aria-label="Photo of four silver keys joined on a ring, lying on a pale blue surface"></div>
      <div class="hero-copy">
        <div class="hero-kicker">MORTGAGE SOFTWARE</div>
        <div class="hero-title">FOR AUSTRALIAN HOME<br>LOAN PROFESSIONALS</div>
        <span class="hero-button">Learn More</span>
      </div>
    </div>
  </div>
</section>

<main class="intro">
  <h2 class="section-title">Welcome to <strong>Quorvane</strong></h2>
  <div class="intro-body">
    <p><b>Quorvane is a leading software player in the Australian mortgage industry</b> with over 10 years industry track record as a proven innovator.</p>
    <p>Quorvane has been responsible for numerous industry firsts in the evolution of its suite of tools and services to mortgage industry professionals including</p>
    <ul class="firsts">
      <li>First 3rd party electronic application platform based on MDXA (2003)</li>
      <li>First direct to consumer MDXA based online application (2006)</li>
      <li>First 'built for industry' product data hub (2009)</li>
    </ul>
    <p>Our platform has been integrated to every major lender in the market as well as almost half the major aggregators in the broker space. We also provide a range of services to 3rd party platform providers in our unique partnered services model.</p>
    <p>We have strong industry connections and an excellent understanding of the industry, how it operates and who operates within it. We were a key member in the original set up of the industry standard, MDXA (www.mdxa.example.org.au) and are one of its key advocates in todays market.</p>
    <p>Numerous banks, including majors from the 'big four' rely daily on Quorvane platform to deliver efficiency, cost savings and true business benefit to their bottom line</p>
  </div>
</main>

<aside class="news">
  <h2 class="section-title">Latest <strong>News</strong></h2>
  <div class="news-list">
    <article class="news-item"><h3>Quorvane launches new enterprise pricing for Rate Compass</h3><time>FRIDAY, JANUARY 8, 2010 AT 3:00PM</time></article>
    <article class="news-item"><h3>New Data Hub to Boost Broker Efficiencies</h3><time>THURSDAY, DECEMBER 3, 2009 AT 3:36PM</time></article>
    <article class="news-item"><h3>Quorvane Names New GM</h3><time>THURSDAY, DECEMBER 3, 2009 AT 3:31PM</time></article>
    <article class="news-item"><h3>Quorvane launches Industry first Product Hub - Rate Compass</h3><time>TUESDAY, JUNE 2, 2009 AT 3:00PM</time></article>
    <div class="news-more"><span class="mark">❖</span>Read More News<span class="mark">❖</span></div>
  </div>
</aside>

<aside class="contact">
  <h2 class="section-title">Contact <strong>Us</strong></h2>
  <div class="contact-card">
    <div class="contact-visual" role="img" aria-label="Illustration of an open mailbox filled with letters"></div>
    <dl class="contact-lines">
      <dt>SALES</dt><dd>02 5550 1482</dd>
      <dt>SUPPORT</dt><dd>1300 555 274</dd>
      <dt>OFFICE LOCATION</dt><dd>Level 14 62 Harwick Lane<br>Eastvale NSW 2079</dd>
    </dl>
  </div>
</aside>

<footer class="site-footer">
  <div class="footer-nav">
    <a href="#">Home</a><span class="sep">|</span><a href="#">Mortgage Solutions</a><span class="sep">|</span><a href="#">Messaging</a><span class="sep">|</span><a href="#">Company</a><span class="sep">|</span><a href="#">News</a><span class="sep">|</span><a href="#">Support</a><span class="sep">|</span><a href="#">Privacy Policy</a><span class="sep">|</span><a href="#">Site Map</a><span class="sep">|</span><a href="#">Contact Us</a>
  </div>
  <div class="legal">© 2009, Quorvane Group Inc. All rights reserve</div>
</footer>
</body>
</html>
```